Brenvick Holdings LLC, new Business cards

I'm moving offices and need new cards. Plus I'm open to modifying the current design of my card. I will keep the logo but would like to explore other layouts and fonts for the design. I've included the current double sided card for reference. I Like the navy color and white. Might be open to grays or silver. Needs to be clean and elegant.

Target Market(s)

Investors, buyers & sellers of private equities and real estate.

Contact Information for Business Card

Brenvick Holdings
Dorian P.K. Halvers, Managing Principal
418 Ostrander Ave., Suite 612
Denver, CO 80319
M: 970-555-0147, O: 303-555-0192
Dorian@brenvickholdings.example
Brenvickholdings.example

Colors
0354a2
ffffff
c4c4c4

Requirements
Must have
• Business card details.
• Logo raised or embossed, it was designed after a wax seal. Current has raised ink.
Nice to have
• Space on card to write additional notes.

```html
<!DOCTYPE html>
<html lang="en">
<head>
<meta charset="utf-8">
<title>Brenvick Holdings – Business Cards</title>
<link rel="stylesheet" href="https://fonts.googleapis.com/css2?family=Mulish:wght@400;600&family=Libre+Baskerville&display=swap">
<style>
  :root {
    --navy: #29244f;
    --white: #ffffff;
    --silver: #c4c4c4;
    --grey-text: #a9a9ad;
    --stage: #e6e6ea;
    --rule: #dedee2;
    --dots: #6d6d78;
  }
  * { box-sizing: border-box; margin: 0; padding: 0; }
  html, body { width: 1200px; height: 880px; overflow: hidden; }
  body {
    background: var(--stage);
    font-family: "Mulish", Arial, sans-serif;
    color: var(--navy);
    position: relative;
  }
  .card {
    position: absolute;
    top: 142px;
    width: 340px;
    height: 595px;
    background: var(--white);
    border-radius: 22px;
    overflow: hidden;
    box-shadow: 0 10px 30px rgba(20, 20, 40, 0.18);
  }
  .card--back { left: 220px; }
  .card--front { left: 640px; }

  .card__footer {
    position: absolute;
    left: 0; right: 0; bottom: 0;
    height: 70px;
    border-top: 9px solid var(--silver);
    background: var(--navy);
    display: flex;
    align-items: center;
    justify-content: center;
  }
  .card__website {
    color: var(--white);
    font-size: 15px;
    letter-spacing: 0.4px;
  }

  .brand {
    display: flex;
    align-items: center;
    gap: 10px;
  }
  .brand__dot {
    border-radius: 50%;
    background: var(--navy);
    flex: none;
  }
  .brand__name {
    font-weight: 600;
    color: var(--navy);
    text-transform: uppercase;
    letter-spacing: 1.5px;
  }

  .front__brand {
    position: absolute;
    top: 48px;
    right: 30px;
  }
  .front__brand .brand__dot { width: 70px; height: 70px; }
  .front__brand .brand__name { font-size: 15px; line-height: 1.25; width: 110px; }

  .contact {
    position: absolute;
    top: 206px;
    left: 40px;
    right: 36px;
  }
  .contact__name {
    font-family: "Libre Baskerville", Georgia, serif;
    font-weight: 400;
    font-size: 17px;
    letter-spacing: 1px;
    text-transform: uppercase;
    color: var(--navy);
  }
  .contact__title {
    font-size: 13px;
    color: var(--grey-text);
    margin-top: 3px;
  }
  .contact__list { list-style: none; margin-top: 18px; }
  .contact__item {
    padding: 7px 0 8px;
    border-bottom: 1px solid var(--rule);
  }
  .contact__item:last-child { border-bottom: none; }
  .contact__label {
    display: block;
    font-size: 11px;
    color: var(--grey-text);
  }
  .contact__value {
    display: block;
    font-size: 14px;
    color: var(--navy);
    line-height: 1.35;
  }

  .note__heading {
    position: absolute;
    top: 48px;
    left: 0; right: 0;
    text-align: center;
    font-size: 15px;
    font-weight: 400;
    letter-spacing: 2px;
    color: var(--navy);
  }
  .note__lines {
    position: absolute;
    top: 108px;
    left: 34px;
    right: 34px;
    list-style: none;
  }
  .note__line {
    height: 30px;
    border-bottom: 2px dotted var(--dots);
  }
  .back__brand {
    position: absolute;
    left: 34px;
    bottom: 104px;
  }
  .back__brand .brand__dot { width: 40px; height: 40px; }
  .back__brand .brand__name { font-size: 10px; line-height: 1.25; width: 80px; }
</style>
</head>
<body>

  <section class="card card--back" aria-label="Card back with note lines">
    <h2 class="note__heading">NOTE</h2>
    <ul class="note__lines">
      <li class="note__line"></li><li class="note__line"></li><li class="note__line"></li>
      <li class="note__line"></li><li class="note__line"></li><li class="note__line"></li>
      <li class="note__line"></li><li class="note__line"></li><li class="note__line"></li>
      <li class="note__line"></li>
    </ul>
    <div class="brand back__brand">
      <span class="brand__dot"></span>
      <span class="brand__name">Brenvick Holdings</span>
    </div>
    <footer class="card__footer"><span class="card__website">Brenvickholdings.example</span></footer>
  </section>

  <section class="card card--front" aria-label="Card front with contact details">
    <div class="brand front__brand">
      <span class="brand__dot"></span>
      <span class="brand__name">Brenvick Holdings</span>
    </div>
    <div class="contact">
      <h1 class="contact__name">Dorian P.K. Halvers</h1>
      <p class="contact__title">Managing Principal</p>
      <ul class="contact__list">
        <li class="contact__item"><span class="contact__label">Mobile:</span><span class="contact__value">970-555-0147</span></li>
        <li class="contact__item"><span class="contact__label">Office:</span><span class="contact__value">303-555-0192</span></li>
        <li class="contact__item"><span class="contact__label">Email:</span><span class="contact__value">Dorian@brenvickholdings.example</span></li>
        <li class="contact__item"><span class="contact__value">418 Ostrander Ave., Suite 612<br>Denver, CO 80319</span></li>
      </ul>
    </div>
    <footer class="card__footer"><span class="card__website">Brenvickholdings.example</span></footer>
  </section>

</body>
</html>
```